Alternative Country Rock Band Needs Website Design

Milo R and The Drifthands Web Design Proposal

Overview
We essentially need design and code for an uncluttered, easy to navigate, simple to access repository for our music, videos, photos, up and coming shows, merchandise, and links to social media. It will be a platform for our fans, new and old to get to the heart of who we are and what we are doing. We want something that will embody our essence as musicians, our distinct flavor, and values. We must be able to add, remove and edit content without developer help.

*If we receive a design so good that it justifies no code, we are open to that*

Friendloop
It would be nice to have Friendloop integration so that much of the site can be liked, possibly commented on but most importantly shared.

This could also possibly be done on Swirlpad http://www.swirlpad.example/ which posts right to Chirpline feeds and Friendloop with cross links back.

Smart Phone
We need the site to be compatible with smart phones.

Branding/Aesthetics

We are really keen on aesthetics. We are almost more concerned about the feel of the site than content, which of course will be there.

We want to aim at an edgy, gritty, folky rock ‘n’ roll with a cowboy kick ambiance. We want the space to have a Southwestern romanticism risqué tinge. We want something that feels similar to our new EP album cover “Dust On Gold.”

Our image is huge and we want people, agents, managers, venues, friends, family, and fans to see who we are immediately and be able to easily connect to us, share us, and contact us.

Content

Our EchoDistrict and Friendloop already exists, so much of it can essentially be reworked into the new site.

We want an About; Shows; Music; Videos (maybe combine as just “Music” so that we don’t clutter the site); Photos; Media/Press (one of the two); Store; Contact Us (booking inquiries etc.) and Easy Big Connectors to Social Media; Email List (somewhere, probably not in navigation)

Examples

These are band sites that we think more or less hit the nail on the head. When reviewing them, it seems we are drawn to sites that have very large pictures, large, easy to use navigation buttons and such.

http://paulvantross.example/

http://www.harborandkin.example/

http://thegreyheron.example/

http://www.mavelinsound.example/site/

http://www.thecrookedpath.example/ (love the size of the photos but don’t like the small navigation)

Hosting
Nimbra has been recommended and it is free, but let us know if you know a better one.

Content Management
We want to be able to upload our shows using EchoDistrict and that they will show on our website, likely by using an RSS Feed. It might even be nice if music, photos and videos could also be linked. Basic Ruby on Rails has been recommended for content management, making it easier to add and remove content, but maybe you know better.

However, we are open to Block Frame or Zop as a prefabricated content management system as well.

Latest Technologies
We need the site up to date with the latest technologies out there, rss feeds, and so on so it will show up on search engines.
Updates

Project Deadline Extended
Reason: A number of designers accepted the job and are yet to submit their work.

Project Deadline Extended
Reason: We are looking for some original design elements. It seems many have over utilized our pictures to supplement design. We've added another $200 on top of the original $300 for a total of $500 for the project. We look forward to your participation!

We've added $200 to bring the total to $500 for our web design.  We are looking forward to your ideas...

Hi Designers,

We've added some more band pictures and posters for inspiration for possible designs.  We look forward to your submissions!

Milo R

Industry/Entity Type

Store

Font styles to use
Sans Serif
Decorative

```html
<!DOCTYPE html>
<html lang="en">
<head>
<meta charset="utf-8">
<title>Milo R and The Drifthands — Official Band Website</title>
<link rel="stylesheet" href="https://fonts.googleapis.com/css2?family=Rye&family=Open+Sans:wght@400;600;700&display=swap">
<style>
:root{
  --ink:#231812;
  --night:#2a1d15;
  --bark:#5a3a22;
  --rust:#8a4a22;
  --copper:#a35a2a;
  --tan:#e6cc98;
  --paper:#efdcb4;
  --sand:#d9bd86;
  --cream:#f6ecd6;
  --orange:#dd8a2a;
  --na:#e9c98a;
  --white:#ffffff;
  --wood-a:#b9b2a6;
  --wood-b:#d8d2c6;
}
*{box-sizing:border-box;margin:0;padding:0}
html,body{width:1200px;height:3348px;overflow:hidden}
body{font-family:"Open Sans",Arial,sans-serif;color:var(--white);background:var(--night)}
.page{position:relative;width:1200px;height:3348px}
.western{font-family:"Rye",Georgia,serif}

/* section headings */
.section-title{display:flex;align-items:center;justify-content:center;gap:22px;font-family:"Rye",Georgia,serif;font-size:34px;letter-spacing:1px;text-transform:uppercase}
.section-title::before,.section-title::after{content:"";width:150px;height:3px;background:currentColor;opacity:.9}
.section-title span::before,.section-title span::after{content:"•";margin:0 14px}
.view-all{display:flex;align-items:center;justify-content:center;gap:18px;font-size:26px;letter-spacing:1px;text-transform:uppercase}
.view-all::before,.view-all::after{content:"";width:60px;height:2px;background:currentColor;opacity:.7}

/* hero */
.hero{position:absolute;top:0;left:0;width:1200px;height:660px}
.hero-photo{position:absolute;inset:0;background:radial-gradient(ellipse at 60% 35%,#8a6a52 0%,#5a3e2c 40%,#2a1c14 100%)}
.brand{position:absolute;left:28px;top:14px;font-family:"Rye",Georgia,serif;font-size:40px;color:var(--white)}
.main-nav{position:absolute;right:0;top:0;width:660px;height:88px;background:rgba(25,17,12,.85);display:flex;justify-content:flex-end;align-items:stretch}
.main-nav a{display:flex;align-items:center;padding:0 22px;font-size:20px;color:var(--white);text-decoration:none;text-transform:uppercase}
.main-nav a.active{background:rgba(255,255,255,.14)}
.hero-title{position:absolute;top:360px;width:100%;text-align:center;font-family:"Rye",Georgia,serif;font-size:68px;text-transform:uppercase;letter-spacing:2px}
.hero-sub{position:absolute;top:478px;width:100%;text-align:center;font-size:26px;letter-spacing:4px;text-transform:uppercase}
.hero-sub::before,.hero-sub::after{content:"•";margin:0 16px}
.hero-down{position:absolute;top:604px;left:572px}

/* band members */
.members{position:absolute;top:660px;left:0;width:1200px;height:640px;background:repeating-linear-gradient(180deg,var(--wood-b) 0 78px,var(--wood-a) 78px 80px);color:var(--ink)}
.members .section-title{position:absolute;top:28px;width:100%}
.member-card{position:absolute;width:262px;height:252px;background:var(--tan);border:3px solid #c7a66a;box-shadow:0 4px 8px rgba(0,0,0,.35);text-align:center;padding:14px 16px}
.member-card .name{font-family:"Rye",Georgia,serif;font-size:30px;color:var(--ink)}
.member-card .portrait{height:140px;margin-top:8px;background:linear-gradient(135deg,#3c4a6a,#7a6a8a 55%,#c48a4a)}
.member-card .role{font-family:"Rye",Georgia,serif;font-size:20px;margin-top:10px;text-transform:uppercase}
.hat-still{position:absolute;left:912px;top:380px;width:250px;height:250px;background:radial-gradient(ellipse at 50% 60%,#efe6d6 0%,#c9a274 45%,rgba(150,100,60,0) 75%)}

/* events */
.events{position:absolute;top:1300px;left:0;width:1200px;height:520px}
.events-photo{position:absolute;inset:0;background:linear-gradient(180deg,#3a2a22,#6a4a36 50%,#3a2820)}
.events-shade{position:absolute;inset:0;background:rgba(20,12,8,.45)}
.events .section-title{position:absolute;top:48px;width:100%}
.events-table{position:absolute;top:130px;left:56px;width:1090px;border-collapse:collapse;font-size:24px}
.events-table th{text-align:left;font-size:32px;font-weight:600;padding:0 8px 10px;border-bottom:2px solid rgba(255,255,255,.6)}
.events-table td{padding:6px 8px;height:46px;border-bottom:1px solid rgba(255,255,255,.35)}
.ticket{display:inline-block;width:100px;text-align:center;font-size:20px;padding:1px 0;background:var(--orange);color:var(--ink)}
.ticket.na{background:var(--na)}
.events .view-all{position:absolute;top:462px;width:100%}

/* gallery */
.gallery{position:absolute;top:1820px;left:0;width:1200px;height:420px;background:linear-gradient(180deg,var(--paper),var(--sand));color:var(--ink)}
.gallery .section-title{position:absolute;top:34px;width:100%}
.album{position:absolute;top:124px;width:260px;height:176px;background:var(--cream);text-align:center}
.album .shot{height:112px}
.album .title{font-size:22px;font-weight:600;margin-top:8px;line-height:1.1}
.album .count{font-size:17px}
.gallery .view-all{position:absolute;top:360px;width:100%;color:var(--copper)}

/* video */
.video{position:absolute;top:2240px;left:0;width:1200px;height:472px}
.video-photo{position:absolute;inset:0;background:linear-gradient(90deg,#1f1713,#4a3a30 60%,#8a7a6a 85%,#3a2c24)}
.video .section-title{position:absolute;top:32px;width:100%}
.player{position:absolute;top:136px;left:320px;width:560px;height:296px;background:#111;border:2px solid #333}
.player-bar{height:28px;font-size:16px;padding:4px 10px;color:#ddd;background:#1c1c1c}
.player-screen{height:236px;background:radial-gradient(ellipse at 50% 40%,#6fa6e8 0%,#2a4a8a 40%,#0a1020 100%)}
.player-controls{height:28px;background:#2a2a2a}
.slide-arrow{position:absolute;top:250px}

/* contact */
.contact{position:absolute;top:2712px;left:0;width:1200px;height:468px;background:var(--rust)}
.contact .section-title{position:absolute;top:32px;width:100%}
.field{position:absolute;left:72px;width:400px;height:40px;background:var(--white);color:#999;font-size:17px;padding:9px 12px}
.required{position:absolute;left:490px;font-size:16px;color:#f1d4b4}
.field.message{height:140px}
.send{position:absolute;left:376px;top:400px;width:216px;height:40px;background:var(--night);color:var(--white);font-size:20px;text-align:center;line-height:40px}
.contact-info{position:absolute;left:632px;top:100px;font-size:22px}
.contact-info h3{font-size:22px;font-weight:400;text-transform:uppercase;margin-bottom:14px}
.contact-info li{list-style:none;display:flex;align-items:center;gap:14px;height:48px}
.map{position:absolute;left:632px;top:296px;width:528px;height:152px;background:linear-gradient(135deg,#e8e4d8,#cfd9c4 50%,#a9c4e0)}

/* footer */
.site-footer{position:absolute;top:3180px;left:0;width:1200px;height:168px;background:var(--night);text-align:center}
.to-top{position:absolute;top:-22px;left:578px;width:44px;height:44px;border-radius:50%;background:var(--white);color:var(--ink);font-size:15px;font-weight:700;line-height:44px}
.social{position:absolute;top:66px;width:100%;display:flex;justify-content:center;gap:28px;font-size:18px;color:var(--tan)}
.social span{display:flex;align-items:center;gap:8px}
.social span::before{content:"";width:18px;height:18px;border-radius:50%;background:var(--copper)}
.copyright{position:absolute;top:124px;width:100%;font-size:16px;color:#bba}
</style>
</head>
<body>
<div class="page">

  <header class="hero">
    <div class="hero-photo" role="img" aria-label="Band photo: six members standing on a city street at dusk"></div>
    <div class="brand">LOGO</div>
    <nav class="main-nav">
      <a class="active" href="#">Home</a><a href="#">About</a><a href="#">Events</a><a href="#">Gallery</a><a href="#">Videos</a><a href="#">Contact</a>
    </nav>
    <h1 class="hero-title">Milo R and The Drifthands</h1>
    <p class="hero-sub">Official Band Website</p>
    <svg class="hero-down" width="56" height="30" viewBox="0 0 56 30"><polyline points="4,4 28,26 52,4" fill="none" stroke="#fff" stroke-width="4"/></svg>
  </header>

  <section class="members">
    <h2 class="section-title"><span>Band Members</span></h2>
    <div class="member-card" style="left:148px;top:100px"><div class="name">John Doe</div><div class="portrait" role="img" aria-label="Singer playing guitar on stage"></div><div class="role">Singer</div></div>
    <div class="member-card" style="left:470px;top:100px"><div class="name">John Doe</div><div class="portrait" role="img" aria-label="Guitarist on stage"></div><div class="role">Guitar</div></div>
    <div class="member-card" style="left:790px;top:100px"><div class="name">John Doe</div><div class="portrait" role="img" aria-label="Drummer behind the kit"></div><div class="role">Drums</div></div>
    <div class="member-card" style="left:308px;top:372px"><div class="name">John Doe</div><div class="portrait" role="img" aria-label="Singer with guitar"></div><div class="role">Singer</div></div>
    <div class="member-card" style="left:630px;top:372px"><div class="name">John Doe</div><div class="portrait" role="img" aria-label="Singer with guitar"></div><div class="role">Singer</div></div>
    <div class="hat-still" role="img" aria-label="Cowboy hat resting on boots"></div>
  </section>

  <section class="events">
    <div class="events-photo" role="img" aria-label="Band seated together in a dim room"></div>
    <div class="events-shade"></div>
    <h2 class="section-title"><span>Upcoming Events</span></h2>
    <table class="events-table">
      <thead><tr><th style="width:200px">Date</th><th style="width:356px">Location</th><th style="width:360px">Venue</th><th>Tickets</th></tr></thead>
      <tbody>
        <tr><td>15/05/2014</td><td>Vienna, Austria</td><td>Mesa Bloom Festival</td><td><span class="ticket na">N/A</span></td></tr>
        <tr><td>07/06/2014</td><td>Zurich, Switzerland</td><td>Ridgeway Arena</td><td><span class="ticket">Tickets</span></td></tr>
        <tr><td>16/06/2014</td><td>London, United Kingdom</td><td>Cedar Hall Center</td><td><span class="ticket">Tickets</span></td></tr>
        <tr><td>10/07/2014</td><td>Paris, France</td><td>Lantern Center</td><td><span class="ticket">Tickets</span></td></tr>
        <tr><td>10/07/2014</td><td>Copenhagen, Denmark</td><td>Saffron Sound Festival</td><td><span class="ticket na">N/A</span></td></tr>
      </tbody>
    </table>
    <div class="view-all">View All</div>
  </section>

  <section class="gallery">
    <h2 class="section-title"><span>Image Gallery</span></h2>
    <div class="album" style="left:68px"><div class="shot" role="img" aria-label="Crowd at a party gig" style="background:linear-gradient(135deg,#3a1a4a,#c0302a 60%,#f08a2a)"></div><div class="title">Party Rock Monday</div><div class="count">17 photos</div></div>
    <div class="album" style="left:348px"><div class="shot" role="img" aria-label="Concert crowd under red lights" style="background:linear-gradient(135deg,#2a0a0a,#c8281a 55%,#f0a030)"></div><div class="title">Amsterdam Concert</div><div class="count">35 photos</div></div>
    <div class="album" style="left:612px"><div class="shot" role="img" aria-label="Performer on a lit stage" style="background:radial-gradient(circle at 50% 30%,#f0e0a0,#c86020 40%,#200a08)"></div><div class="title">On Stage</div><div class="count">21 photos</div></div>
    <div class="album" style="left:880px"><div class="shot" role="img" aria-label="Band recording inside the studio" style="background:linear-gradient(135deg,#1a2a6a,#c03a6a 55%,#f0a040)"></div><div class="title">Inside Our Studio</div><div class="count">25 photos</div></div>
    <div class="view-all">View All</div>
  </section>

  <section class="video">
    <div class="video-photo" role="img" aria-label="Close-up of guitar tuning pegs"></div>
    <h2 class="section-title"><span>Video Gallery</span></h2>
    <svg class="slide-arrow" style="left:64px" width="34" height="80" viewBox="0 0 34 80"><polyline points="30,4 4,40 30,76" fill="none" stroke="#fff" stroke-width="4"/></svg>
    <div class="player">
      <div class="player-bar">Live At The Canyon Session Highlights</div>
      <div class="player-screen" role="img" aria-label="Video still of a singer on a blue-lit stage"></div>
      <div class="player-controls"></div>
    </div>
    <svg class="slide-arrow" style="left:1102px" width="34" height="80" viewBox="0 0 34 80"><polyline points="4,4 30,40 4,76" fill="none" stroke="#fff" stroke-width="4"/></svg>
  </section>

  <section class="contact">
    <h2 class="section-title"><span>Contact Us</span></h2>
    <div class="field" style="top:136px">Full name</div><div class="required" style="top:146px">required</div>
    <div class="field" style="top:184px">Email</div><div class="required" style="top:194px">required</div>
    <div class="field" style="top:232px">Subject</div>
    <div class="field message" style="top:284px;width:520px">Message</div>
    <div class="send">Send message</div>
    <div class="contact-info">
      <h3>Contact Info</h3>
      <ul>
        <li><svg width="20" height="26" viewBox="0 0 20 26"><path d="M10 1C5 1 1 5 1 10c0 7 9 15 9 15s9-8 9-15c0-5-4-9-9-9z" fill="#fff"/><circle cx="10" cy="10" r="3.5" fill="#8a4a22"/></svg>1234 Street name, New York, New York</li>
        <li><svg width="22" height="22" viewBox="0 0 22 22"><path d="M5 1l4 5-2 3c1 3 3 5 6 6l3-2 5 4-3 4C9 21 1 13 1 4z" fill="#fff"/></svg>1234-567-890</li>
        <li><svg width="24" height="18" viewBox="0 0 24 18"><rect x="1" y="1" width="22" height="16" fill="#fff"/><polyline points="1,1 12,10 23,1" fill="none" stroke="#8a4a22" stroke-width="2"/></svg>bandname@mail.com</li>
      </ul>
    </div>
    <div class="map" role="img" aria-label="Street map showing the band office location"></div>
  </section>

  <footer class="site-footer">
    <div class="to-top">UP</div>
    <div class="social"><span>Friendloop</span><span>Chirpline</span><span>Reelbox</span><span>Circlet</span><span>Linkwork</span></div>
    <p class="copyright">© 2014 All Rights Reserved.</p>
  </footer>

</div>
</body>
</html>
```